Meridale Sonography Academy (Meridale Institute of Scan Studies) needs an additional web design f

Don't require a redesign of our existing website, I need an additional web design to compliment and feed into our existing web page (kplv.edu.au) but establish excellent google rankings in it's own right. Web page is to appeal to a specific target market in the allied health industry who wish to learn how to do ultrasound on patients. New website is www. rapidsonarskillsnet.com.au. Our educational institution delivers hands on workshops and seminars on ANYTHING involved with EMERGENCY Ultrasound - intro, advanced, doctors, nurses, etc. Our competitors in this field www.scanlearnhub.com.au and www.bqo.edu.au. Looking for a design that will capture the target audience and deliver the message that the courses are delivered by one of the best faculties in Australia. SEO strategies are paramount in that we don't wish to be penalised by Google by running a feeder site. Courses are delivered in Sydney and are accredited by an organisation called TVRE.com.au. The courses are listed under 2 qualifications on TVRE website - PLDX and RWMTZ. Registrants of our courses are striving to achieve either PLDX - Diploma in Bedside Operator Scan Skills http://www.tvre.com.au/newsite/Files/Documents/Education/PLDX/PLDX_Course_Brochure.pdf OR RWMTZ - Diploma in Support Staff Operated Scan Skills http://www.tvre.com.au/newsite/Files/Documents/Education/RWMTZ/RWMTZ_Course_Brochure.pdf.
Website to be iphone, smartphone and tablet compatible.

Target Market(s)

Emergency Physicians and Emergency nurses/doctors.

Industry/Entity Type

School

Coding

Coded - Design and coding required

Number of Pages Required

2 page

Font styles to use
Other font styles liked:
• See website http://www.brightfolddental.com.au/

Colors
86cae6
ec1f27

Requirements
Must have
• Overall professional feel but easy to read and informative.
• Links to our normal website pages www.kplv.edu.au
• Ability to rank high.
• Copy of material we deliver here http://www.kplv.edu.au/acute-scan-class-1-3-days/ Click through on relevant dates for more information.
Nice to have
• I like this website - font, feel, layout etc.
• http://www.brightfolddental.com.au/
Should not have
• Information that will lower our google rankings knowing it is linked to www.kplv.edu.au

```html
<!DOCTYPE html>
<html lang="en">
<head>
<meta charset="utf-8">
<title>Rapid Sonar Skills</title>
<link rel="stylesheet" href="https://fonts.googleapis.com/css2?family=Lato:ital,wght@0,400;0,700;1,400&family=Raleway:wght@500;600&display=swap">
<style>
:root{
  --red:#ec1f27;
  --blue:#86cae6;
  --blue-dark:#4fb0d8;
  --ink:#2b2b2b;
  --text:#555;
  --grey-bg:#eeeeee;
  --line:#dcdcdc;
  --footer:#333333;
  --footer-base:#242424;
  --white:#fff;
}
*{box-sizing:border-box;margin:0;padding:0}
html,body{width:676px;height:1200px;overflow:hidden}
body{font-family:'Lato',sans-serif;color:var(--text);background:var(--white);position:relative}
.abs{position:absolute}
.top-rule{left:0;top:0;width:676px;height:2px;background:var(--red)}
.header{left:0;top:2px;width:676px;height:55px;background:linear-gradient(#fff,#f1f1f1)}
.brand{left:74px;top:15px;font-family:'Raleway',sans-serif;font-weight:600;color:var(--red);font-size:20px;line-height:24px;white-space:nowrap}
.helpline{left:441px;top:14px;width:162px;height:31px;border:1px solid #d8d8d8;border-radius:4px;background:#fafafa}
.helpline .avatar{left:8px;top:-3px;width:24px;height:32px;border-radius:12px 12px 2px 2px;background:linear-gradient(#5a4a44,#cfd6dc)}
.helpline p{left:38px;top:5px;font-size:7.5px;line-height:11px;color:#666}
.helpline span{color:var(--blue-dark)}
.nav{left:0;top:57px;width:676px;height:27px;background:var(--blue)}
.nav ul{list-style:none;position:absolute;left:74px;top:0;display:flex;height:27px}
.nav li{color:#fff;font-size:9.2px;font-weight:700;line-height:27px;padding:0 6px;border-left:1px solid #a6d8ec;text-transform:uppercase}
.nav li:first-child{border-left:0;background:var(--red);padding:0 8px}
.hero{left:0;top:84px;width:676px;height:236px;background:linear-gradient(100deg,#cfd9e0 0%,#eef2f4 35%,#c8b7a6 60%,#e7ecef 85%,#b9c6cf 100%)}
.search{left:443px;top:86px;width:158px;height:20px;background:var(--red);border:1px solid #f78a8e}
.search span{position:absolute;left:7px;top:5px;font-size:7px;font-style:italic;color:#fde;}
.search svg{position:absolute;right:7px;top:4px}
.caption{left:389px;top:242px;height:35px}
.caption .bar{left:0;top:0;width:4px;height:35px;background:var(--red)}
.caption .box{left:4px;top:0;width:208px;height:35px;background:rgba(134,202,230,.82)}
.caption p{position:absolute;left:6px;top:1px;color:#fff;font-family:'Raleway',sans-serif;font-weight:600;font-size:14.5px;line-height:16.5px;white-space:nowrap}
.welcome{left:0;top:320px;width:676px;height:130px}
.welcome h1{position:absolute;left:74px;width:528px;top:19px;text-align:center;font-family:'Raleway',sans-serif;font-weight:600;font-size:16.5px;color:var(--ink)}
.welcome h1 .r{color:var(--red)} .welcome h1 .b{color:var(--blue-dark)}
.welcome .rule{position:absolute;left:74px;top:41px;width:528px;height:1px;background:var(--line)}
.welcome .lead{position:absolute;left:74px;width:528px;top:48px;text-align:center;font-weight:700;font-size:8.4px;line-height:12px;color:#222}
.welcome .body{position:absolute;left:74px;width:528px;top:78px;text-align:center;font-size:7.4px;line-height:11.3px;color:#555}
.services{left:0;top:450px;width:676px;height:147px;background:var(--grey-bg);border-top:1px solid #e2e2e2;border-bottom:1px solid #e2e2e2}
.service{top:14px;width:130px;text-align:center}
.service .ring{width:70px;height:70px;margin:0 auto;border:3px solid var(--red);border-radius:50%;background:#fff;display:flex;align-items:center;justify-content:center}
.service h3{font-size:9.8px;font-weight:700;color:var(--ink);margin-top:8px}
.service p{font-size:7.6px;line-height:10.5px;margin-top:4px;color:#444}
.news{left:0;top:597px;width:676px;height:193px}
.col{top:14px;width:253px}
.col h2{font-family:'Raleway',sans-serif;font-weight:600;font-size:12.5px;color:var(--ink)}
.col h2 em{font-style:normal;color:var(--red)}
.col .dots{margin-top:4px;border-bottom:1px dotted #bbb}
.item{position:relative;height:74px;border-bottom:1px solid #eee;margin-top:0}
.item .date{position:absolute;top:10px;font-size:7.6px;font-weight:700;color:#333}
.item .title{position:absolute;top:21px;font-size:7.4px;color:var(--blue-dark)}
.item .text{position:absolute;top:33px;font-size:7.4px;line-height:11px;color:#555}
.item .thumb{position:absolute;left:0;top:9px;width:44px;height:50px;border:1px solid #ccc;padding:2px;background:#fff}
.item .thumb div{width:100%;height:100%}
.testimonials{left:0;top:790px;width:676px;height:160px;background:#e9e9e9}
.testimonials h2{position:absolute;left:0;width:676px;top:17px;text-align:center;font-family:'Raleway',sans-serif;font-weight:600;font-size:14px;color:var(--ink)}
.testimonials h2 em{font-style:normal;color:var(--red)}
.testimonials .sub{position:absolute;left:0;width:676px;top:38px;text-align:center;font-size:8.4px;color:#777}
.stars{left:322px;top:53px}
.portrait{left:77px;top:74px;width:64px;height:64px;border-radius:50%;border:3px solid var(--red);background:linear-gradient(#c9d3db,#e8edf0)}
.quote{left:152px;top:80px;width:448px;font-size:7.3px;line-height:12.4px;font-style:italic;color:#444;text-indent:14px}
.cite{left:152px;top:126px;font-size:7.4px;font-style:italic;font-weight:700;color:#777}
.more{left:520px;top:126px;font-size:7.6px;color:#333;text-decoration:underline}
.affiliates{left:0;top:950px;width:676px;height:103px}
.affiliates h2{position:absolute;left:0;width:676px;top:14px;text-align:center;font-family:'Raleway',sans-serif;font-weight:600;font-size:13px;color:var(--ink)}
.affiliates h2 em{font-style:normal;color:var(--red)}
.affiliates .lines{position:absolute;left:96px;top:22px;width:484px;height:1px;background:linear-gradient(90deg,transparent,#ccc 30%,transparent 35%,transparent 65%,#ccc 70%,transparent)}
.badge{top:42px;width:95px;height:45px;border:1px solid #ddd;background:#fff;padding:3px}
.badge div{width:100%;height:100%;background:#f0f0f0;display:flex;align-items:center;justify-content:center}
.footer{left:0;top:1053px;width:676px;height:130px;background:var(--footer);color:#ddd}
.footer h4{font-size:8.6px;font-weight:400;color:#fff;text-transform:uppercase;letter-spacing:.3px}
.fcol{top:16px}
.fcol ul{list-style:none;margin-top:11px}
.fcol li{font-size:7.8px;line-height:17.2px;color:#eee}
.contact-row{position:relative;padding-left:16px;font-size:7.6px;line-height:10px;margin-top:10px;color:#eee}
.contact-row svg{position:absolute;left:0;top:0}
.contact-row b{color:#fff}
.news-form p{font-size:7.3px;line-height:10.4px;margin-top:9px}
.field{width:121px;height:15px;background:#fff;margin-top:4px;font-size:6.8px;color:#888;padding:3px 4px}
.btn{display:inline-block;background:var(--red);color:#fff;font-size:7.4px;font-weight:700;padding:3px 7px;margin-top:6px}
.social{position:relative;height:24px;margin-top:8px;padding-left:28px}
.social .dot{position:absolute;left:0;top:0;width:21px;height:21px;border-radius:50%}
.social b{display:block;font-size:8.2px;color:#fff;font-weight:400;text-transform:uppercase;padding-top:2px}
.social small{display:block;font-size:5.6px;color:#bbb;letter-spacing:.4px;text-transform:uppercase}
.base{left:0;top:1183px;width:676px;height:17px;background:var(--footer-base);text-align:center;font-size:6.6px;line-height:17px;color:#ccc}
</style>
</head>
<body>
<div class="abs top-rule"></div>

<header class="abs header">
  <div class="abs brand">Rapid Sonar Skills</div>
  <div class="abs helpline">
    <div class="abs avatar" role="img" aria-label="Photo of a support advisor wearing a headset"></div>
    <p class="abs">Need a helping hand? Call our office<br>for advice - <span>1800 555 0199</span></p>
  </div>
</header>

<nav class="abs nav">
  <ul>
    <li>Home</li><li>About Us</li><li>Seminars</li><li>Become a Sonographer</li><li>Consulting</li><li>Models</li><li>Information</li><li>Contact Us</li>
  </ul>
</nav>

<section class="abs hero" role="img" aria-label="Photo of three clinicians in lab coats studying a monitor in a laboratory"></section>
<div class="abs search">
  <span>Search anything&nbsp; here.......</span>
  <svg width="11" height="11" viewBox="0 0 11 11"><circle cx="4.5" cy="4.5" r="3.3" fill="none" stroke="#fff" stroke-width="1.5"/><line x1="7" y1="7" x2="10" y2="10" stroke="#fff" stroke-width="1.6"/></svg>
</div>
<div class="abs caption">
  <div class="abs bar"></div>
  <div class="abs box"><p>WE TEACH HOW TO DO<br>ULTRASOUND ON PATIENTS</p></div>
</div>

<section class="abs welcome">
  <h1>WELCOME TO <span class="r">RAPID SONAR</span> <span class="b">SKILLS</span></h1>
  <div class="rule"></div>
  <p class="lead">Lorem ipsum dolor sit amet, consectetur adipiscing elit. Suspendisse porttitor, turpis at dapibus semper, lacus odio ultricies ante, vulputate congue libero enim et nulla. In interdum imperdiet odio. Morbi aliquet feugiat lacus, id mollis velit euismod sit amet.</p>
  <p class="body">Lorem ipsum dolor sit amet, consectetur adipiscing elit. Vivamus vel dolor vel urna elementum sodales. Curabitur placerat, nisl vitae rhoncus consectetur, augue velit imperdiet justo, vel euismod turpis sem ut dolor. Quisque eros ex, laoreet aliquam tellus in, congue finibus augue. Nam neque mi, congue malesuada arcu eget, elementum dignissim est. Suspendisse luctus laoreet nisl at lobortis. Curabitur sit amet tempus diam. Ut hendrerit consectetur porttitor.</p>
</section>

<section class="abs services">
  <div class="abs service" style="left:64px">
    <div class="ring"><svg width="36" height="36" viewBox="0 0 36 36"><circle cx="13" cy="8" r="4" fill="#86cae6"/><rect x="7" y="13" width="12" height="14" rx="3" fill="#86cae6"/><line x1="19" y1="17" x2="31" y2="7" stroke="#86cae6" stroke-width="2"/><rect x="4" y="27" width="22" height="3" fill="#86cae6"/></svg></div>
    <h3>Seminars and Training</h3>
    <p>Loremipsumdolorsitamet,consect eturadipiscingelit. Morbifrin</p>
  </div>
  <div class="abs service" style="left:202px">
    <div class="ring"><svg width="38" height="32" viewBox="0 0 38 32"><path d="M19 30 L3 8 Q19 -2 35 8 Z" fill="#86cae6"/><ellipse cx="19" cy="16" rx="6" ry="4" fill="#fff"/></svg></div>
    <h3>Become a Sonographer</h3>
    <p>Loremipsumdolorsitamet,consect eturadipiscingelit. Morbifrin</p>
  </div>
  <div class="abs service" style="left:341px">
    <div class="ring"><svg width="32" height="36" viewBox="0 0 32 36"><rect x="4" y="4" width="20" height="28" rx="2" fill="none" stroke="#86cae6" stroke-width="2"/><path d="M8 12h4M8 18h4M8 24h4" stroke="#86cae6" stroke-width="2"/><path d="M14 12h6M14 18h6M14 24h6" stroke="#86cae6" stroke-width="1.4"/><line x1="28" y1="8" x2="20" y2="26" stroke="#86cae6" stroke-width="2.4"/></svg></div>
    <h3>Register to KPLV</h3>
    <p>Loremipsumdolorsitamet,consect eturadipiscingelit. Morbifrin</p>
  </div>
  <div class="abs service" style="left:480px">
    <div class="ring"><svg width="34" height="32" viewBox="0 0 34 32"><rect x="7" y="3" width="24" height="26" rx="2" fill="none" stroke="#86cae6" stroke-width="2"/><path d="M7 10H3v16a3 3 0 0 0 6 0" fill="none" stroke="#86cae6" stroke-width="2"/><rect x="11" y="7" width="16" height="5" fill="#86cae6"/><path d="M11 16h16M11 20h16M11 24h10" stroke="#86cae6" stroke-width="1.5"/></svg></div>
    <h3>Venue Information</h3>
    <p>Loremipsumdolorsitamet,consect eturadipiscingelit. Morbifrin</p>
  </div>
</section>

<section class="abs news">
  <div class="abs col" style="left:74px">
    <h2>UPCOMING <em>NEWS AND EVENTS</em></h2>
    <div class="dots"></div>
    <div class="item">
      <svg class="abs" style="left:0;top:11px" width="12" height="12" viewBox="0 0 12 12"><rect x="1" y="2" width="10" height="9" fill="none" stroke="#86cae6"/><path d="M1 5h10M4 5v6M7 5v6M1 8h10" stroke="#86cae6" stroke-width=".7"/></svg>
      <span class="date" style="left:17px">03 May, 2014</span>
      <span class="title" style="left:17px">LOREM IPSUM DOLOR SIT AMNSECTETUR</span>
      <p class="text" style="left:17px;width:236px">Lorem ipsum dolor sit amet, consectetur adipiscing elit. Sed blandit mas massa vel mauris sollicitudin dignissim. Phasellus ultrices tellus egethop ipsum ornare molestie scelerisque eros.</p>
    </div>
    <div class="item" style="border-bottom:0">
      <svg class="abs" style="left:0;top:11px" width="12" height="12" viewBox="0 0 12 12"><rect x="1" y="2" width="10" height="9" fill="none" stroke="#86cae6"/><path d="M1 5h10M4 5v6M7 5v6M1 8h10" stroke="#86cae6" stroke-width=".7"/></svg>
      <span class="date" style="left:17px">03 May, 2014</span>
      <span class="title" style="left:17px">LOREM IPSUM DOLOR SIT AMNSECTETUR</span>
      <p class="text" style="left:17px;width:236px">Lorem ipsum dolor sit amet, consectetur adipiscing elit. Sed blandit mas massa vel mauris sollicitudin dignissim. Phasellus ultrices tellus egethop ipsum ornare molestie scelerisque eros.</p>
    </div>
  </div>
  <div class="abs col" style="left:349px">
    <h2>UPCOMING <em>SEMINARS</em></h2>
    <div class="dots"></div>
    <div class="item">
      <div class="thumb"><div role="img" aria-label="Portrait photo of a female presenter" style="background:linear-gradient(#6b5548,#e5e2df)"></div></div>
      <span class="date" style="left:53px">03 May, 2014</span>
      <span class="title" style="left:53px">LOREM IPSUM DOLOR SIT AMNSECTETUR</span>
      <p class="text" style="left:53px;width:200px">Lorem ipsum dolor sit amet, consectetur adipiscing elit. Sedn blandit mas massa vel mauris sollicitudin dignissim. Pselluso ultrices tellus egethop ipsum ornare molestie.</p>
    </div>
    <div class="item" style="border-bottom:0">
      <div class="thumb"><div role="img" aria-label="Portrait photo of a male presenter in a suit" style="background:linear-gradient(#e8e6e3,#2f3440)"></div></div>
      <span class="date" style="left:53px">03 May, 2014</span>
      <span class="title" style="left:53px">LOREM IPSUM DOLOR SIT AMNSECTETUR</span>
      <p class="text" style="left:53px;width:200px">Lorem ipsum dolor sit amet, consectetur adipiscing elit. Sedn blandit mas massa vel mauris sollicitudin dignissim. Pselluso ultrices tellus egethop ipsum ornare molestie.</p>
    </div>
  </div>
</section>

<section class="abs testimonials">
  <h2>WHAT PEOPLE <em>SAY ABOUT US</em></h2>
  <p class="sub">Lorem ipsum dolor sit amet, consectetur Donec a consequat mag&nbsp; Aenean eu velit&nbsp; Aenean sollicitudin</p>
  <svg class="abs stars" width="32" height="9" viewBox="0 0 32 9">
    <g fill="#ec1f27"><path d="M4.5 0l1.3 3h3.2l-2.6 2 1 3.2-2.9-2-2.9 2 1-3.2L0 3h3.2z"/><path transform="translate(11.5 0)" d="M4.5 0l1.3 3h3.2l-2.6 2 1 3.2-2.9-2-2.9 2 1-3.2L0 3h3.2z"/><path transform="translate(23 0)" d="M4.5 0l1.3 3h3.2l-2.6 2 1 3.2-2.9-2-2.9 2 1-3.2L0 3h3.2z"/></g>
  </svg>
  <div class="abs portrait" role="img" aria-label="Portrait photo of the reviewer"></div>
  <p class="abs quote">Lorem sum dolor sit amet, consectetuer adipiscing elit, sed diam nonummy nibh euismod tincidunt ut laoreet dolore magna aliquam erat volutpat. Ut wisi enim ad minim veniam, quis nostrud exerci tation ullamcorper suscipit lobortis nisl ut aliquip commodo consequat. Duis autem vel eum iriure dolor in hendrerit in vulputate velit esse molestie consequat, vel illum dolore eu feugiat nulla facilisis at vero eros et accumsan et iusto</p>
  <span class="abs cite">.... Daren Kole, Helixworks , USA</span>
  <span class="abs more">Read more testimonials »</span>
</section>

<section class="abs affiliates">
  <div class="lines"></div>
  <h2>WE ARE <em>AFFILIATED WITH</em></h2>
  <div class="abs badge" style="left:74px"><div><svg width="40" height="20"><rect width="40" height="20" fill="#d9c3c4"/></svg></div></div>
  <div class="abs badge" style="left:183px"><div><svg width="40" height="20"><rect width="40" height="20" fill="#c4dbe6"/></svg></div></div>
  <div class="abs badge" style="left:291px"><div><svg width="22" height="22"><circle cx="11" cy="11" r="10" fill="#c9d4c4"/></svg></div></div>
  <div class="abs badge" style="left:399px"><div><svg width="22" height="22"><rect width="22" height="22" fill="#e0c6c0"/></svg></div></div>
  <div class="abs badge" style="left:507px"><div><svg width="22" height="22"><rect width="22" height="22" fill="#c8cbe0"/></svg></div></div>
</section>

<footer class="abs footer">
  <div class="abs fcol" style="left:74px">
    <h4>Quick Link</h4>
    <ul><li>Home</li><li>About Us</li><li>Seminars</li><li>Seminar</li><li>Contact Us</li></ul>
  </div>
  <div class="abs fcol" style="left:178px;width:150px">
    <h4>Contact Address</h4>
    <div class="contact-row"><svg width="9" height="12" viewBox="0 0 9 12"><path d="M4.5 0A4.5 4.5 0 0 0 0 4.5C0 8 4.5 12 4.5 12S9 8 9 4.5A4.5 4.5 0 0 0 4.5 0z" fill="#fff"/><circle cx="4.5" cy="4.5" r="1.6" fill="#333"/></svg><b>The KPLV office is located at:</b><br>Suite 210, Larkfield House 4 Corran St<br>Wexley NSW, 2099</div>
    <div class="contact-row"><svg width="8" height="11" viewBox="0 0 8 11"><rect width="8" height="11" rx="1.5" fill="#fff"/><rect x="1.5" y="1.5" width="5" height="6" fill="#333"/></svg>+ 61 2 5550 1234</div>
    <div class="contact-row" style="margin-top:6px"><svg width="10" height="9" viewBox="0 0 10 9"><rect x="2" y="0" width="6" height="3" fill="#fff"/><rect x="0" y="3" width="10" height="4" fill="#fff"/><rect x="2" y="6" width="6" height="3" fill="#fff" stroke="#333" stroke-width=".6"/></svg>+ 61 2 5550 5678</div>
    <div class="contact-row" style="margin-top:6px"><svg width="10" height="8" viewBox="0 0 10 8"><rect width="10" height="8" fill="#fff"/><path d="M0 0l5 4 5-4" fill="none" stroke="#333" stroke-width=".8"/></svg>admin@kplv.edu.au</div>
  </div>
  <div class="abs fcol news-form" style="left:342px;width:125px">
    <h4>Newsletter Signup</h4>
    <p>Signup with us and get update in your inbox.</p>
    <div class="field">Your Name</div>
    <div class="field" style="margin-top:5px">Email address</div>
    <span class="btn">Subscribe</span>
  </div>
  <div class="abs fcol" style="left:508px;width:95px">
    <h4>Social Connect</h4>
    <div class="social" style="margin-top:10px"><span class="dot" style="background:#3b5998"></span><b>Kinfeed</b><small>Become a fan</small></div>
    <div class="social"><span class="dot" style="background:#dd4b39"></span><b>Orbitly</b><small>Add to circles</small></div>
    <div class="social"><span class="dot" style="background:#f7931e"></span><b>RSS Feed</b><small>Subscribe now</small></div>
  </div>
</footer>
<div class="abs base">Copyright 2014, KPLV. All rights reserved.</div>
</body>
</html>
```